Retail Consultant Business Card Design

We're looking to update the look of our very old business cards. We work primarily in the fast paced retail industry, and would like a business card that won't look dated after a few years.

We are consultants that focus primarily on shopping malls (80%), or mixed use developments (20% shopping + office space + residential). That being the case, we know that there is a lot of room for creativity. We are not a law firm, so the design doesn't have to be very static or serious. We are also not a clothing brand, so it shouldn't be too "out there" (lipstick font, jean jacket background....etc).

We're looking for something more "middle of the road", with the design leaning more towards the creative side. Our consulting firm is not very big, so we are very open to breaking away from the "traditional" or simple business card model.

One last thing that might help you, is to know who we generally hand these cards out to. It really ranges from Developers to Architects, to actual retail brands like Vela, K&T, Marbrook, Tug & Fox, Lumiva...etc.

Contact Information for Business Card

Company Name: (Northwind Venture Partners Global, LLC)
Individuals Name & Title
Company Address: (287 W. Alder Lane, Suite C, Tustin, CA 92781)
Telephone Number: (714) 555-0182
Fax Number: (714) 555-0376
Website: nvpglobal-example.net
Email

Font styles to use
Serif

Colors

Designer to choose colors to be used in the design.

Requirements
Must have
• 1. The incorporation of our logo in whatever way you think would work. We have no requirements for how this should happen.
• 2. Space in the back for a QR Code, with space for instructions like
• "save us as a contact on your mobile" (or something to that effect). This will allow our clients to scan the information on the card into their phones for quick contact creation. Obviously we will handle the whole QR Code issue, but if you could mock it up , so that we could get a sense of how it would look.
• 3. Try and use brighter colors, instead of darker ones. This is really up to you, the darker colors might make other colors pop. I just mention this, because we are trying to give the sense of energy or movement, if that makes any sense.
• 4. Obviously, space for all the normal business card text (Company name, person name, phone number, email.....etc)

```html
<!DOCTYPE html>
<html lang="en">
<head>
<meta charset="utf-8">
<title>Northwind Venture Partners Global – Business Card</title>
<link href="https://fonts.googleapis.com/css2?family=Roboto:wght@400;500;700&display=swap" rel="stylesheet">
<style>
  :root {
    --page-bg: #e9e7e4;
    --card-top: #f7f7f6;
    --card-bottom: #e4e6e7;
    --brand-blue: #2a7fc1;
    --brand-blue-deep: #1f6bab;
    --brand-cyan: #3a9ad6;
    --accent-red: #d9262a;
    --accent-yellow: #f0b21a;
    --wave-white: #fbfaf7;
    --name-cream: #ecdfc7;
    --title-cream: #f1e7d6;
    --ink: #1d1d1f;
    --icon-blue: #2f86c4;
  }
  html, body {
    margin: 0;
    width: 1200px;
    height: 1054px;
    overflow: hidden;
    background: var(--page-bg);
    font-family: "Roboto", Arial, sans-serif;
  }
  .card {
    position: absolute;
    left: 100px;
    top: 224px;
    width: 1000px;
    height: 605px;
    background: linear-gradient(160deg, var(--card-top), var(--card-bottom));
    box-shadow: 0 6px 22px rgba(0,0,0,0.18);
    overflow: hidden;
  }
  .header-art {
    position: absolute;
    left: 0;
    top: 0;
    width: 100%;
    height: 204px;
    background: linear-gradient(90deg,
      rgba(217,38,42,0.35) 0%,
      rgba(240,178,26,0.35) 25%,
      var(--brand-cyan) 55%,
      var(--brand-blue) 100%);
  }
  .card-text {
    position: absolute;
    inset: 0;
    display: block;
    width: 100%;
    height: 100%;
  }
  .person-name { font: 700 30px "Roboto", Arial, sans-serif; fill: var(--name-cream); }
  .person-title { font: 400 19px "Roboto", Arial, sans-serif; fill: var(--title-cream); }
  .contact-line { font: 400 19px "Roboto", Arial, sans-serif; fill: var(--ink); }
  .company-name { font: 500 21px "Roboto", Arial, sans-serif; fill: var(--brand-blue-deep); }
  .icon { fill: var(--icon-blue); }
</style>
</head>
<body>
  <div class="card">
    <div class="header-art" role="img" aria-label="Decorative blue header band with red and yellow flowing swooshes"></div>

    <svg class="card-text" viewBox="0 0 785 475" xmlns="http://www.w3.org/2000/svg">
      <text class="person-name" x="737" y="68" text-anchor="end">Elliot Marsh Reyes</text>
      <text class="person-title" x="737" y="99" text-anchor="end">Managing Director</text>

      <g class="company-mark">
        <circle cx="74" cy="268" r="22" fill="var(--brand-cyan)"/>
        <text class="company-name" x="108" y="260">Northwind Venture</text>
        <text class="company-name" x="108" y="288">Partners Global</text>
      </g>

      <text class="contact-line" x="737" y="264" text-anchor="end">287 W. Alder Lane, Suite C,</text>
      <text class="contact-line" x="737" y="292" text-anchor="end">Tustin, CA 92781</text>

      <text class="contact-line" x="698" y="347" text-anchor="end">(714) 555-0182</text>
      <text class="contact-line" x="698" y="375" text-anchor="end">(714) 555-0376</text>
      <text class="contact-line" x="698" y="403" text-anchor="end">www.nvpglobal-example.net</text>
      <text class="contact-line" x="698" y="431" text-anchor="end">name@nvpglobal-example.net</text>

      <g class="icon" transform="translate(716 333)">
        <path d="M2 6 C2 2 18 2 18 6 L18 8 L14 8 L14 6 L6 6 L6 8 L2 8 Z"/>
        <rect x="4" y="9" width="12" height="8" rx="1.5"/>
      </g>
      <g class="icon" transform="translate(716 361)">
        <rect x="5" y="1" width="10" height="5"/>
        <rect x="2" y="6" width="16" height="8" rx="1.5"/>
        <rect x="5" y="12" width="10" height="6"/>
      </g>
      <g transform="translate(716 391)">
        <rect class="icon" x="1" y="1" width="18" height="13" rx="1"/>
        <path d="M1 2 L10 9 L19 2" fill="none" stroke="var(--wave-white)" stroke-width="1.5"/>
      </g>
      <g transform="translate(726 426)">
        <circle class="icon" r="8.5"/>
        <ellipse rx="3.5" ry="8.5" fill="none" stroke="var(--wave-white)" stroke-width="1.2"/>
        <path d="M-8.5 0 H8.5 M-7 -4 H7 M-7 4 H7" stroke="var(--wave-white)" stroke-width="1.2"/>
      </g>
    </svg>
  </div>
</body>
</html>
```